Tarwin Project Consulting

I need a logo and business card design for a small business operating in the management consulting and contractor space, predominantly in local and state government. I specialise in project management, financial consulting, people and culture, procurement, ICT transformation and contracting for corporate support areas of organisations.

Industry/Entity Type

Business

```html
<!DOCTYPE html>
<html lang="en">
<head>
<meta charset="utf-8">
<title>Tarwin Project Consulting – Business Card</title>
<link rel="stylesheet" href="https://fonts.googleapis.com/css2?family=Cabin:ital,wght@0,400;0,600;1,400&display=swap">
<style>
  :root {
    --page: #ffffff;
    --card-deep: #123f9e;
    --card-mid: #1c4bb0;
    --card-light: #2656b8;
    --band-line: #3f6fd0;
    --band-fill: rgba(70, 120, 215, 0.25);
    --text-main: #ffffff;
    --text-soft: #e6edfb;
    --accent: #8fc3ee;
    --shadow: rgba(10, 20, 50, 0.35);
  }
  * { margin: 0; padding: 0; box-sizing: border-box; }
  html, body {
    width: 1005px;
    height: 1200px;
    overflow: hidden;
    background: var(--page);
    font-family: "Cabin", "Segoe UI", sans-serif;
  }
  .card {
    position: absolute;
    left: 51px;
    width: 859px;
    height: 500px;
    background: linear-gradient(160deg, var(--card-light) 0%, var(--card-mid) 45%, var(--card-deep) 100%);
    box-shadow: 10px 14px 28px var(--shadow);
    color: var(--text-main);
    overflow: hidden;
  }
  .card--front { top: 51px; }
  .card--back { top: 606px; }

  .band {
    position: absolute;
    left: 0;
    right: 0;
    height: 18px;
    background: var(--band-fill);
    border-top: 2px solid var(--band-line);
    border-bottom: 2px solid var(--band-line);
  }
  .card--front .band { top: 352px; }
  .card--back .band { top: 130px; }

  /* Front */
  .brand-mark {
    position: absolute;
    left: 78px;
    top: 150px;
    display: flex;
    align-items: center;
    gap: 18px;
  }
  .brand-mark__dot {
    width: 70px;
    height: 70px;
    border-radius: 50%;
    background: var(--accent);
  }
  .brand-mark__name {
    font-weight: 600;
    font-size: 34px;
    letter-spacing: 2px;
    color: var(--accent);
  }
  .contact {
    position: absolute;
    right: 66px;
    top: 78px;
    text-align: right;
  }
  .contact__name {
    font-weight: 600;
    font-size: 38px;
    letter-spacing: 0.5px;
    line-height: 1;
  }
  .contact__role {
    font-style: italic;
    font-size: 31px;
    margin-top: 14px;
    color: var(--text-soft);
  }
  .contact__line {
    display: flex;
    justify-content: flex-end;
    align-items: center;
    gap: 14px;
    font-size: 33px;
    line-height: 1;
  }
  .contact__line--phone { margin-top: 40px; }
  .contact__line--email { margin-top: 20px; }
  .contact__line svg { fill: none; stroke: var(--text-main); stroke-width: 2.4; }
  .address {
    position: absolute;
    right: 66px;
    top: 412px;
    font-size: 28px;
    color: var(--text-soft);
  }

  /* Back */
  .brand-header {
    position: absolute;
    left: 70px;
    top: 32px;
    display: flex;
    align-items: center;
    gap: 80px;
  }
  .brand-header__dot {
    width: 72px;
    height: 72px;
    border-radius: 50%;
    background: var(--accent);
  }
  .brand-header__name {
    font-weight: 600;
    font-size: 33px;
    letter-spacing: 2.5px;
    text-transform: uppercase;
    color: var(--text-soft);
  }
  .services {
    position: absolute;
    left: 226px;
    top: 174px;
    list-style: none;
  }
  .services__item {
    position: relative;
    padding-left: 56px;
    font-size: 27px;
    line-height: 40px;
    text-transform: uppercase;
    letter-spacing: 0.5px;
    color: var(--text-soft);
  }
  .services__item::before {
    content: "\2666";
    position: absolute;
    left: 0;
    top: 0;
    font-size: 20px;
  }
</style>
</head>
<body>

<section class="card card--front" aria-label="Business card front">
  <div class="brand-mark">
    <span class="brand-mark__dot"></span>
    <span class="brand-mark__name">TARWIN</span>
  </div>

  <div class="contact">
    <p class="contact__name">PETER LAWSON</p>
    <p class="contact__role">Director</p>
    <p class="contact__line contact__line--phone">
      <svg width="20" height="30" viewBox="0 0 20 30" aria-hidden="true">
        <rect x="2" y="2" width="16" height="26" rx="2"/>
        <line x1="2" y1="21" x2="18" y2="21"/>
      </svg>
      <span>9123 45678</span>
    </p>
    <p class="contact__line contact__line--email">
      <svg width="32" height="22" viewBox="0 0 32 22" aria-hidden="true">
        <rect x="2" y="2" width="28" height="18"/>
        <polyline points="2,2 16,13 30,2"/>
      </svg>
      <span>hello@tarwinpc.com</span>
    </p>
  </div>

  <div class="band"></div>

  <p class="address">14 Harbour Lane, Northbridge NSW 2063</p>
</section>

<section class="card card--back" aria-label="Business card back">
  <div class="brand-header">
    <span class="brand-header__dot"></span>
    <span class="brand-header__name">Tarwin Project Consulting</span>
  </div>

  <div class="band"></div>

  <ul class="services">
    <li class="services__item">Project Management</li>
    <li class="services__item">Financial Consulting</li>
    <li class="services__item">People and Culture</li>
    <li class="services__item">Procurement</li>
    <li class="services__item">ICT Transformation</li>
    <li class="services__item">Corporate Support Areas<br>of Organisations</li>
  </ul>
</section>

</body>
</html>
```